Business Card Design

We are an IT staffing and consulting company providing IT solutions and resources to our clients.

Industry/Entity Type

Business

Contact Information for Business Card

Ravindra Kolluparthi
Vice President

BrimTrail Inc
48260 Hollyfern Market Court, suite 700
Ashburn, VA 20147
Direct: 571-555-0193
Mobile: 571-555-0147
Email: Ravindra@brimtrailinc.example
Fax: 703-555-0162
www.brimtrailinc.example

```html
<!DOCTYPE html>
<html lang="en">
<head>
<meta charset="utf-8">
<title>BrimTrail Inc — Business Card</title>
<link rel="stylesheet" href="https://fonts.googleapis.com/css2?family=Open+Sans:wght@400;600;700&display=swap">
<style>
  :root {
    --bg: #9a9a9a;
    --card: #f7f7f7;
    --card-shade: #e9e9e9;
    --ink: #3a3a3a;
    --ink-soft: #555555;
    --red: #c8102e;
    --black: #111111;
    --white: #ffffff;
    --rule: #d6d6d6;
  }
  * { box-sizing: border-box; margin: 0; padding: 0; }
  html, body {
    width: 1200px; height: 894px; overflow: hidden;
    background: var(--bg);
    font-family: "Open Sans", Arial, sans-serif;
  }
  .canvas {
    width: 1200px; height: 894px;
    display: flex; flex-direction: column; align-items: center; justify-content: center;
    gap: 30px;
  }
  .card {
    position: relative;
    width: 720px; height: 411px;
    background: linear-gradient(135deg, var(--white) 0%, var(--card) 55%, var(--card-shade) 100%);
    box-shadow: 0 6px 18px rgba(0,0,0,.25);
    overflow: hidden;
  }
  .stripe { position: absolute; top: 0; bottom: 0; display: flex; }
  .stripe--left { left: 0; }
  .stripe--right { right: 0; flex-direction: row-reverse; }
  .stripe__dark { width: 10px; background: var(--black); }
  .stripe__accent { width: 4px; background: var(--red); }

  /* front */
  .contact-list {
    position: absolute; left: 50px; top: 110px;
    list-style: none;
  }
  .contact-list li {
    display: flex; align-items: center; gap: 14px;
    font-size: 16px; line-height: 34px; color: var(--ink-soft);
    white-space: nowrap;
  }
  .contact-list svg {
    width: 16px; height: 16px; flex: none;
    fill: none; stroke: var(--red); stroke-width: 1.6;
    stroke-linecap: round; stroke-linejoin: round;
  }
  .person { position: absolute; left: 50px; top: 290px; }
  .person__name { font-size: 22px; font-weight: 700; color: var(--ink); white-space: nowrap; }
  .person__title { font-size: 16px; color: var(--red); margin-top: 2px; }

  .divider {
    position: absolute; left: 370px; top: 40px; width: 1px; height: 250px;
    background: linear-gradient(to bottom, transparent, var(--rule), transparent);
  }
  .company { position: absolute; left: 400px; top: 100px; }
  .brand {
    display: flex; align-items: center; gap: 12px; white-space: nowrap;
  }
  .brand__dot {
    width: 16px; height: 16px; border-radius: 50%; background: var(--red); flex: none;
  }
  .brand__name {
    font-size: 32px; font-weight: 600; color: var(--ink); letter-spacing: 1px;
  }
  .address {
    margin-top: 34px; font-size: 14px; line-height: 24px; color: var(--ink);
    white-space: nowrap;
  }
  .website {
    margin-top: 24px; font-size: 14px; font-weight: 700; color: var(--red); letter-spacing: 2px;
    white-space: nowrap;
  }

  /* back */
  .card--back .brand {
    position: absolute; left: 50%; top: 50%; transform: translate(-50%, -50%);
  }
  .card--back .brand__dot { width: 24px; height: 24px; }
  .card--back .brand__name { font-size: 52px; }
</style>
</head>
<body>
<main class="canvas">

  <section class="card card--front" aria-label="Business card front">
    <div class="stripe stripe--left" aria-hidden="true">
      <span class="stripe__dark"></span><span class="stripe__accent"></span>
    </div>

    <ul class="contact-list">
      <li>
        <svg viewBox="0 0 16 16" aria-hidden="true"><path d="M3 2.5 L6 2 L7.5 5.5 L5.8 6.8 Q7 9.3 9.2 10.2 L10.5 8.5 L14 10 L13.5 13 Q7.5 14 3.5 9 Q1.8 6 3 2.5 Z"/></svg>
        571-555-0193
      </li>
      <li>
        <svg viewBox="0 0 16 16" aria-hidden="true"><rect x="4.5" y="1.5" width="7" height="13" rx="1.2"/><path d="M7 12 h2"/></svg>
        571-555-0147
      </li>
      <li>
        <svg viewBox="0 0 16 16" aria-hidden="true"><rect x="1.5" y="6" width="13" height="6" rx="1"/><path d="M4.5 6 V2 H11.5 V6 M4.5 10 V14 H11.5 V10"/></svg>
        703-555-0162
      </li>
      <li>
        <svg viewBox="0 0 16 16" aria-hidden="true"><rect x="1.5" y="3.5" width="13" height="9" rx="1"/><path d="M1.8 4 L8 8.5 L14.2 4"/></svg>
        Ravindra@brimtrailinc.example
      </li>
    </ul>

    <div class="person">
      <p class="person__name">Ravindra Kolluparthi</p>
      <p class="person__title">Vice President</p>
    </div>

    <div class="divider"></div>

    <div class="company">
      <div class="brand">
        <span class="brand__dot"></span>
        <span class="brand__name">BrimTrail Inc</span>
      </div>
      <p class="address">48260 Hollyfern Market Court, suite 700<br>Ashburn, VA 20147</p>
      <p class="website">www.brimtrailinc.example</p>
    </div>
  </section>

  <section class="card card--back" aria-label="Business card back">
    <div class="brand">
      <span class="brand__dot"></span>
      <span class="brand__name">BrimTrail Inc</span>
    </div>
    <div class="stripe stripe--right" aria-hidden="true">
      <span class="stripe__dark"></span><span class="stripe__accent"></span>
    </div>
  </section>

</main>
</body>
</html>
```